High value cover design for an A4 ideation pad.

The product is NOT A BOOK.

It's an A4 ideation pad for professionals, designers and creators who handwrite their ideas. Visualise creators like Paul Menteith, Glen Usborne and Carl Whitmoor in your mind's eye.

I'm looking for a cover design for the ideation pad. Both front and back.

It should look, feel and convey the following.

--> A handcrafted product experience

--> High value & Elegance

--> Inspiration

Mandatory --> See Uploaded Files --> Files 1, 5 & 6

Target Market(s)

- Designers

-Creative Professionals

- Entrepreneurs

who handwrite their ideas. Visualise creators like Paul Menteith, Glen Usborne and Carl Whitmoor in your mind's eye.

Industry/Entity Type

Stationary

Font styles to use
Script
Other font styles liked:
• Calligraphy

Colors
fbed22

Requirements
Must have
• Title text - Ink And Iron

-Text in gold on brown leather background to convey high value for the front cover.

--> High value & Elegance

--> Inspiration

--> Should compel the customers to pick up and own the idea pad
Nice to have
• That's my take but other ideas are welcome
Should not have
• Must not convey

- low value

```html
<!DOCTYPE html>
<html lang="en">
<head>
<meta charset="utf-8">
<title>Ink And Iron — Ideation Pad Cover</title>
<link rel="stylesheet" href="https://fonts.googleapis.com/css2?family=Cinzel:wght@400;500&display=swap">
<style>
  :root {
    --bg-glow: #302e1f;
    --bg-mid: #16150e;
    --bg-edge: #020202;
    --gold-light: #fff7a0;
    --gold: #fbed22;
    --gold-deep: #d99a0c;
    --gold-shade: #8a5a05;
  }
  html, body {
    margin: 0;
    padding: 0;
    width: 840px;
    height: 1200px;
    overflow: hidden;
    background: var(--bg-edge);
  }
  .cover {
    position: relative;
    width: 840px;
    height: 1200px;
    overflow: hidden;
    background: radial-gradient(ellipse 520px 560px at 424px 500px,
      var(--bg-glow) 0%, var(--bg-mid) 55%, var(--bg-edge) 100%);
    font-family: "Cinzel", "Trajan Pro", serif;
  }
  .title {
    position: absolute;
    left: 0;
    width: 840px;
    margin: 0;
    text-align: center;
    font-weight: 400;
    line-height: 1;
  }
  .title-line {
    display: block;
    position: absolute;
    left: 0;
    width: 840px;
    text-align: center;
    background: linear-gradient(180deg, var(--gold-light) 0%, var(--gold) 40%, var(--gold-deep) 75%, var(--gold-shade) 100%);
    -webkit-background-clip: text;
    background-clip: text;
    color: transparent;
    filter: drop-shadow(2px 2px 0 #7a4d04) drop-shadow(0 0 14px rgba(251, 237, 34, 0.18));
  }
  .title-line--upper {
    top: 296px;
    font-size: 116px;
    letter-spacing: 2px;
  }
  .title-line--main {
    top: 416px;
    font-size: 168px;
    letter-spacing: 4px;
  }
  .reflection {
    position: absolute;
    left: 0;
    top: 553px;
    width: 840px;
    text-align: center;
    font-size: 168px;
    letter-spacing: 4px;
    line-height: 1;
    color: var(--gold);
    opacity: 0.22;
    transform: scaleY(-1);
    -webkit-mask-image: linear-gradient(0deg, #000 0%, rgba(0,0,0,0.4) 45%, transparent 85%);
    mask-image: linear-gradient(0deg, #000 0%, rgba(0,0,0,0.4) 45%, transparent 85%);
  }
</style>
</head>
<body>
  <main class="cover">
    <h1 class="title">
      <span class="title-line title-line--upper">INK AND</span>
      <span class="title-line title-line--main">IRON</span>
    </h1>
    <div class="reflection" aria-hidden="true">IRON</div>
  </main>
</body>
</html>
```